Ready to be wowed! Snazzy, sassy, classy Realtor seeking Web banner for unique innovative Realtor!

Placer County Realtor need web banner re-design. Looking for classy, classic, clean design appealing to elite prospects. Previous focus was short sales now looking to gear towards listing and selling homes, remove short sale focus. Must include, license # 04729318, HR logo, phone, email, etc. check out LiaPorter.com for reference info. I am open to suggestions for other needed content for THE BEST WEB BANNER ON EARTH! LOL. I really want to appeal to the upscale clients, also will be getting away from orange colors going more to a green. Please contact me at LiaPorterSells@mailvista.com for more info
measurements of banner; Images of exactly 960 × 120 pixels will be used as-is. It's Wordpress Genesis.
Updates

I'm really looking for something clean that looks upscale and luxury, classy. 

Please update email address to lia@liaporter.com

Reason: I still haven't gotten what I want. I noticed some really good designs closer to the end here, I'm hoping to allow those folks and maybe a few new ones the opportunity to give me exactly what I want! Thanks!

Reason: I still don't have what I want. I want a simple design that shows that I am a Realtor, maybe a picture of a house???? or something related to real estate. Less emphasis on the Halverson Realty logo. Classy and upscale. Fonts should be easy to read but not so simply boring. Please, please, please read the brief!! I REALLY want a good banner!!

Please take a look at the site color adjustment. That's what color it will stay. www.LiaPorter.com

Reason: I'm ready to move this to the end now. I need a design. I'm extending hopefully only this last time to take a vote on them. I will be reaching out to a few select designers to make a few modifications. I appreciate everyone's time on this as you know this is a very tough and important decision to make.

Reason: Need more input

Reason: still trying to decide

Target Market(s)

upscale home sellers

Industry/Entity Type

Realtor

Requirements
Must have
• License # 04729318
Phone (555)304-2871
HR LOGO (attached)
areas of service- Roseville, Rocklin, Granite Bay
LiaPorterSells@mailvista.com

```html
<!DOCTYPE html>
<html lang="en">
<head>
<meta charset="utf-8">
<title>Lia Porter – Realtor Banner</title>
<link href="https://fonts.googleapis.com/css2?family=Italianno&family=Arimo:wght@400;700&display=swap" rel="stylesheet">
<style>
  :root {
    --bg-light: #f7f7f7;
    --bg-mid: #e9e9e9;
    --frame-white: #ffffff;
    --name-grey: #3d3b3a;
    --label-green: #7c9a2e;
    --value-dark: #2f2f2f;
    --rule: #d6d6d6;
    --photo-warm: #c9a46a;
    --photo-cool: #6f8fa6;
  }
  html, body {
    margin: 0;
    padding: 0;
    overflow: hidden;
  }
  .banner {
    position: relative;
    width: 1200px;
    height: 150px;
    overflow: hidden;
    background: linear-gradient(170deg, var(--bg-light) 0%, var(--bg-mid) 55%, var(--bg-light) 100%);
    font-family: "Arimo", Arial, sans-serif;
  }
  .banner__swoosh {
    position: absolute;
    inset: 0;
  }
  .brokerage {
    position: absolute;
    left: 14px;
    top: 56px;
    display: flex;
    align-items: center;
    gap: 10px;
  }
  .brokerage__mark {
    width: 16px;
    height: 16px;
    border-radius: 50%;
    background: var(--label-green);
  }
  .brokerage__name {
    color: var(--value-dark);
    font-weight: 400;
    font-size: 26px;
    line-height: 1;
    white-space: nowrap;
  }
  .agent-name {
    position: absolute;
    left: 284px;
    top: 4px;
    margin: 0;
    font-family: "Italianno", cursive;
    font-weight: 400;
    font-size: 112px;
    line-height: 1;
    color: var(--name-grey);
    text-shadow: 1px 2px 2px rgba(0,0,0,0.2);
    white-space: nowrap;
  }
  .agent-email {
    position: absolute;
    left: 531px;
    top: 104px;
    font-size: 16px;
    color: var(--value-dark);
    white-space: nowrap;
  }
  .agent-photo {
    position: absolute;
    left: 765px;
    top: 20px;
    width: 100px;
    height: 110px;
    box-sizing: border-box;
    border: 3px solid var(--frame-white);
    box-shadow: 0 1px 4px rgba(0,0,0,0.3);
    background: linear-gradient(180deg, var(--photo-warm) 0%, #d8b98a 45%, var(--photo-cool) 100%);
  }
  .contact-list {
    position: absolute;
    left: 884px;
    top: 14px;
    width: 300px;
    margin: 0;
    padding: 0;
    list-style: none;
    font-size: 18px;
  }
  .contact-list__item {
    padding: 3px 0 4px;
    border-bottom: 1px solid var(--rule);
    line-height: 1.2;
  }
  .contact-list__item:last-child {
    border-bottom: none;
  }
  .contact-list__label {
    color: var(--label-green);
  }
  .contact-list__value {
    color: var(--value-dark);
  }
</style>
</head>
<body>
  <div class="banner">
    <svg class="banner__swoosh" width="1200" height="150" viewBox="0 0 1200 150" aria-hidden="true">
      <path d="M0 150 C 300 95, 650 70, 1200 120 L1200 150 Z" fill="#ffffff" opacity="0.55"/>
      <path d="M0 40 C 250 10, 520 30, 760 0 L0 0 Z" fill="#ffffff" opacity="0.35"/>
    </svg>

    <div class="brokerage">
      <span class="brokerage__mark"></span>
      <span class="brokerage__name">Halverson Realty</span>
    </div>

    <h1 class="agent-name">Lia Porter</h1>
    <div class="agent-email">LiaPorterSells@mailvista.com</div>

    <div class="agent-photo" role="img" aria-label="Portrait photo of the agent"></div>

    <ul class="contact-list">
      <li class="contact-list__item"><span class="contact-list__label">License #</span> <span class="contact-list__value">04729318</span></li>
      <li class="contact-list__item"><span class="contact-list__label">Phone</span> <span class="contact-list__value">(555)304-2871</span></li>
      <li class="contact-list__item"><span class="contact-list__label">Servicing</span> <span class="contact-list__value">Roseville, Rocklin<br>&amp; Granite Bay</span></li>
    </ul>
  </div>
</body>
</html>
```